*** Business Card Design Project

I need a logo and business card for my new catering business: "Brevano". The design should be modern, clean, elegant and refined. One or Two colours only. The design SHOULD NOT include graphics or images. There should be space for my name, phone number and email address (I will provide these to you later).

Industry/Entity Type

Catering

Requirements
Must have
• Must have one or two colours only.
Must include the text "brevano"
Should not have
• Must not have graphics or images.

```html
<!DOCTYPE html>
<html lang="en">
<head>
<meta charset="UTF-8">
<title>Brevano Business Card</title>
<link rel="stylesheet" href="https://fonts.googleapis.com/css2?family=Arimo:wght@400;700&display=swap">
<style>
  :root {
    --backdrop: #a5643d;
    --brand-top: #b3005f;
    --brand-bottom: #740040;
    --brand: #b0005c;
    --card-white: #ffffff;
    --text-grey: #555555;
    --divider: #8a8a8a;
  }
  * { margin: 0; padding: 0; box-sizing: border-box; }
  html, body {
    width: 1157px;
    height: 1200px;
    overflow: hidden;
  }
  body {
    position: relative;
    background: var(--backdrop);
    font-family: "Arimo", Arial, sans-serif;
  }
  .card {
    position: absolute;
    left: 246px;
    width: 665px;
    height: 411px;
    box-shadow: 0 8px 22px rgba(0, 0, 0, 0.35);
  }
  .card-front {
    top: 134px;
    background: linear-gradient(to bottom, var(--brand-top), var(--brand-bottom));
    display: flex;
    align-items: center;
    justify-content: center;
  }
  .front-wordmark {
    color: var(--card-white);
    font-weight: 700;
    font-size: 86px;
    letter-spacing: 1px;
    margin-top: -22px;
    margin-left: 28px;
  }
  .card-back {
    top: 607px;
    background: var(--card-white);
  }
  .back-wordmark {
    position: absolute;
    left: 66px;
    top: 870px;
    top: 263px;
    color: var(--brand);
    font-weight: 700;
    font-size: 42px;
    line-height: 1;
  }
  .divider {
    position: absolute;
    left: 290px;
    top: 220px;
    width: 2px;
    height: 146px;
    background: var(--divider);
  }
  .contact {
    position: absolute;
    left: 327px;
    top: 247px;
    font-size: 24px;
    line-height: 31px;
    color: var(--text-grey);
  }
  .contact-name { color: var(--brand); }
</style>
</head>
<body>
  <section class="card card-front">
    <div class="front-wordmark">Brevano</div>
  </section>

  <section class="card card-back">
    <div class="back-wordmark">Brevano</div>
    <div class="divider"></div>
    <div class="contact">
      <p class="contact-name">Name Surname</p>
      <p class="contact-email">email@email.com</p>
      <p class="contact-phone">111-222-333</p>
    </div>
  </section>
</body>
</html>
```